organic, healthy living website needs a new home page!

We need a home page for the front page of our website (www.fernmeadowco.com.au).

We want to see the following at a glance! We want to gain trust - communicate value, and navigate visitors to the next step - purchasing!

Our two main products:
- certified organic veggies (weekly in Melbourne, Australia - Mentone, Frankston and Ringwood with more pick up locations to come soon)

-ethical wooden toys (by membership only at this stage - run quarterly as a bulk buy - just for Melbourne people!)

Other products:
- health appliances - juicers, dehydrators and water filters (free delivery to their door all over Australia)

- natural parenting products which promote breastfeeding, homebirth, cosleeping and gentle parenting (books, jewellery, gifts, blessingway etc) all over Australia - send via Southern Parcelway.

This website holds all of our products for purchase. We want to emphasise exactly what is to offer here. We will have an info blog which we want to link THROUGH the product homepage of FM. The blog will include a directory of natural services (for a very niche market), recipes, stories, and a wealth of information to do with natural pregnancy, health, parenting, health and community!

We have 5 images linked below - we need these to correspond with the words PREGNANCY, BIRTH, PARENTING, HEALTH, And COMMUNITY and maybe a little design on these - such as dragonflies or flowers - or both. We will code these to work in a slideshow, and link to our blog.

We want this page to feature everything we do, but also be aesthetically pleasing without overkill. We want it to reflect our style, and vision. Natural, organic, and as close to nature as possible. Flow is important, as is consistency throughout the page. WE want it to appeal to our hippy mamas and papas who just want to love their babies, live organically and as healthy as they can.

We love the look and feel of the following websites:

http://brightlarderhub.com/

Thank you!!

Target Market(s)

20-50 year old parents who are environmentally aware and health conscious. They have very close bonds to their children.
Think bohemian, rustic, vintage yet with a modern feel.

Industry/Entity Type

Health

Font styles to use
Script

Colors
e34197
6b449b
33a6d7
0455a3
33b7a4

Requirements
Must have
• Must be clean and say at a glance exactly what we do.

```html
<!DOCTYPE html>
<html lang="en">
<head>
<meta charset="utf-8">
<title>Fern Meadow Co — Organic living</title>
<link rel="stylesheet" href="https://fonts.googleapis.com/css2?family=Sorts+Mill+Goudy&family=Cormorant+Garamond:wght@500&display=swap">
<style>
:root{
  --teal:#33b7a4;
  --purple:#6b449b;
  --pink:#e34197;
  --sky:#33a6d7;
  --navy:#0455a3;
  --ink:#3a3a3a;
  --white:#ffffff;
  --panel:rgba(255,255,255,0.78);
  --mint:#e6efe8;
}
*{margin:0;padding:0;box-sizing:border-box}
html,body{width:809px;height:1200px;overflow:hidden}
body{font-family:"Sorts Mill Goudy",Georgia,serif;color:var(--ink);position:relative}
.backdrop{position:absolute;inset:0;background:
  radial-gradient(ellipse 260px 200px at 80px 120px,#6f8f4e 0%,rgba(111,143,78,0) 100%),
  radial-gradient(ellipse 330px 260px at 690px 560px,#b9cf7c 0%,rgba(185,207,124,0) 100%),
  radial-gradient(ellipse 300px 260px at 90px 640px,#c7d98c 0%,rgba(199,217,140,0) 100%),
  radial-gradient(ellipse 220px 160px at 130px 930px,#3a4660 0%,rgba(58,70,96,0) 100%),
  linear-gradient(160deg,#8d9a76 0%,#c9ab8b 35%,#d8b998 60%,#cdb7a3 100%)}
.topbar{position:absolute;top:7px;left:460px;display:flex;align-items:center;gap:14px;font-size:8px;color:var(--purple)}
.topbar span::before{content:"";display:inline-block;width:8px;height:8px;border-radius:50%;background:var(--purple);margin-right:4px;vertical-align:-1px}
.search{width:54px;height:14px;border-radius:7px;background:#f3e3ee;border:1px solid var(--pink);font-size:7px;line-height:12px;padding-left:8px;color:#555;position:relative}
.search svg{position:absolute;right:6px;top:2px}
.social{position:absolute;display:flex;gap:3px}
.social i{width:21px;height:21px;border-radius:50%;font-style:normal;font-size:7px;color:#fff;display:flex;align-items:center;justify-content:center}
.social.top i{background:rgba(255,255,255,.35);border:1px solid rgba(255,255,255,.8);color:#fff}
.brand{position:absolute;top:48px;left:0;width:809px;text-align:center;color:var(--white)}
.brand .mark{width:84px;height:84px;border-radius:50%;background:rgba(255,255,255,.9);margin:0 auto}
.brand h1{font-family:"Cormorant Garamond",serif;font-weight:500;font-size:28px;letter-spacing:2px;margin-top:16px}
.mainnav{position:absolute;top:198px;left:155px;width:480px;height:60px;color:var(--white)}
.mainnav div{position:absolute;top:0}
.mainnav h2{font-weight:normal;font-size:11.5px;margin-bottom:6px}
.mainnav p{font-size:9.5px;line-height:10px}
.panel{position:absolute;left:152px;top:275px;width:482px;height:745px;background:var(--panel)}
.emblem{position:absolute;left:50%;transform:translateX(-50%);color:var(--teal);font-size:18px;display:flex;align-items:center;gap:5px}
.emblem::before{content:"";width:10px;height:10px;border-radius:50%;background:var(--teal)}
.intro{position:absolute;top:67px;left:40px;width:402px;text-align:center;font-size:9.5px;line-height:11px}
.feature{position:absolute;top:137px;height:105px}
.feature .photo{width:100%;height:100%}
.feature .tag{position:absolute;bottom:0;height:18px;display:flex;align-items:center;font-size:7px;color:#fff;padding:0 5px;gap:4px}
.arrowbox{width:18px;height:18px;display:flex;align-items:center;justify-content:center}
h3{position:absolute;left:0;width:100%;text-align:center;font-weight:normal;font-size:19px;color:#444}
.deals{position:absolute;left:30px;top:345px;width:418px;height:134px;background:var(--white)}
.product{position:absolute;top:18px;width:96px;text-align:center;font-size:6.5px;line-height:8px}
.product .shot{width:70px;height:78px;margin:0 auto 12px;border-radius:6px}
.nav-dot{position:absolute;top:54px;width:25px;height:25px;border-radius:50%;background:var(--sky);display:flex;align-items:center;justify-content:center}
.quotes{position:absolute;left:30px;top:597px;width:418px;height:101px;background:var(--mint)}
.quote{position:absolute;top:12px;width:110px;text-align:center;font-size:6.5px;line-height:7.5px}
.quote .avatar{width:24px;height:18px;border-radius:12px 12px 2px 2px;background:#4a4440;margin:0 auto 8px}
.viewmore{position:absolute;right:0;bottom:0;display:flex;align-items:center;gap:4px;font-size:6.5px}
footer{position:absolute;left:0;top:1077px;width:809px;height:87px;background:var(--teal);color:var(--white)}
footer .col{position:absolute;top:15px;font-size:6.5px;line-height:8px}
footer h4{font-weight:normal;font-size:9.5px;margin-bottom:2px}
.subscribe{position:absolute;left:504px;top:62px;width:128px;height:15px}
.subscribe .field{position:absolute;left:0;top:0;width:100px;height:15px;border-radius:8px;background:#fff;color:#555;font-size:7px;line-height:15px;padding-left:12px}
.subscribe .send{position:absolute;right:0;top:0;width:38px;height:15px;border-radius:8px;background:var(--purple);color:#fff;font-size:8px;line-height:15px;text-align:center}
.legal{position:absolute;top:1164px;left:0;width:809px;height:36px;background:var(--white)}
.legal p{position:absolute;left:155px;top:12px;font-size:8.5px}
.payments{position:absolute;left:480px;top:8px;display:flex;gap:6px}
.payments span{width:28px;height:17px;border:1px solid #ccc;border-radius:2px;font-size:5.5px;display:flex;align-items:center;justify-content:center;color:var(--navy)}
</style>
</head>
<body>
<div class="backdrop" role="img" aria-label="Photograph of fresh dill, sliced kiwifruit and blueberries on a rustic wooden table"></div>

<div class="topbar"><span>My Account</span><span>Cart is empty</span>
  <div class="search">search<svg width="8" height="8" viewBox="0 0 8 8"><circle cx="3.2" cy="3.2" r="2.3" fill="none" stroke="#e34197" stroke-width="1"/><line x1="5" y1="5" x2="7.5" y2="7.5" stroke="#e34197" stroke-width="1.2"/></svg></div>
</div>
<div class="social top" style="left:528px;top:44px"><i>Ch</i><i>Cl</i><i>Lw</i><i>Cs</i><i>Tw</i></div>

<header class="brand">
  <div class="mark"></div>
  <h1>FERN MEADOW CO</h1>
</header>

<nav class="mainnav">
  <div style="left:0"><h2>Our Certified Products</h2><p>Certified Organic Veggies<br>Wooden Toys</p></div>
  <div style="left:141px"><h2>Health promotion</h2><p>Dehydrators<br>Slow Pressing Juicers<br>Coastline Clayworks<br>Water Filters</p></div>
  <div style="left:270px"><h2>Gifts</h2><p>Blessingway<br>New mama<br>Angel Mama</p></div>
  <div style="left:365px"><h2>Children</h2><p>Books<br>Toys<br>Clothing</p></div>
  <div style="left:443px"><h2>Parents</h2><p>Books<br>Jewellery</p></div>
</nav>

<main class="panel">
  <div class="emblem" style="top:24px">FM</div>
  <p class="intro">Jujubes jelly beans pastry cake biscuit jujubes cheesecake. Chocolate bar chocolate bar topping lemon drops tootsie roll. Macaroon chocolate bar sweet tart powder tootsie roll macaroon liquorice.<br>Bonbon carrot cake tart. Danish dessert danish croissant topping biscuit. Candy lollipop lemon drops tart muffin bear claw gummi bears leafcrate.com carrot cake.</p>

  <div class="feature" style="left:35px;width:201px">
    <div class="photo" role="img" aria-label="Crate of fresh organic carrots, greens and fruit" style="background:linear-gradient(135deg,#c7b08a 0%,#e58a3a 45%,#5f8a3c 75%,#d6c7a8 100%)"></div>
    <div class="tag" style="left:0"><span class="arrowbox" style="background:var(--pink)"><svg width="6" height="8"><path d="M5 1 2 4 5 7" fill="none" stroke="#fff" stroke-width="1.4"/></svg></span>Organic veggies</div>
  </div>
  <div class="feature" style="left:237px;width:210px">
    <div class="photo" role="img" aria-label="Handmade wooden toy animals on white" style="background:linear-gradient(135deg,#fbf8f3 0%,#e9d2b0 45%,#c9a070 60%,#fbf8f3 100%)"></div>
    <div class="tag" style="right:0;color:#555">View more<span class="arrowbox" style="background:var(--purple);border-radius:9px 0 0 0"><svg width="6" height="8"><path d="M1 1 4 4 1 7" fill="none" stroke="#fff" stroke-width="1.4"/></svg></span></div>
  </div>

  <div class="emblem" style="top:270px">FM</div>
  <h3 style="top:318px">Hot deals</h3>
  <section class="deals">
    <div class="product" style="left:6px"><div class="shot" role="img" aria-label="Product photo of a black countertop blender" style="background:radial-gradient(ellipse 26px 38px at 50% 55%,#2a2a2a 0%,#6a6a6a 60%,rgba(255,255,255,0) 100%)"></div>Whirlwind Blender<br>by Pure Pantry</div>
    <div class="product" style="left:112px"><div class="shot" role="img" aria-label="Product photo of a silver slow juicer" style="background:radial-gradient(ellipse 26px 38px at 50% 55%,#9a9a9a 0%,#d4d4d4 60%,rgba(255,255,255,0) 100%)"></div>Pressa PE Elite Juicer</div>
    <div class="product" style="left:214px"><div class="shot" role="img" aria-label="Product photo of a chrome and black slow juicer" style="background:radial-gradient(ellipse 26px 38px at 50% 55%,#4a4a4a 0%,#bdbdbd 60%,rgba(255,255,255,0) 100%)"></div>Pressa PS-22 (PS series) juicer</div>
    <div class="product" style="left:316px"><div class="shot" role="img" aria-label="Product photo of a red slow juicer" style="background:radial-gradient(ellipse 26px 38px at 50% 55%,#8e1a1a 0%,#cf3a3a 60%,rgba(255,255,255,0) 100%)"></div>PRESSA PR-D40<br>(PR500) juicer</div>
    <span class="nav-dot" style="left:-14px"><svg width="8" height="10"><path d="M6 1 2 5 6 9" fill="none" stroke="#fff" stroke-width="1.8"/></svg></span>
    <span class="nav-dot" style="right:-14px"><svg width="8" height="10"><path d="M2 1 6 5 2 9" fill="none" stroke="#fff" stroke-width="1.8"/></svg></span>
  </section>

  <div class="emblem" style="top:522px">FM</div>
  <h3 style="top:570px">Testimonials</h3>
  <section class="quotes">
    <div class="quote" style="left:17px"><div class="avatar" role="img" aria-label="Customer portrait"></div>"My family has been very fortunate to have access to super fresh organic fruit and veggies at a..."<br>– Jess Holloway (Chatter),<br>03/05/2014</div>
    <div class="quote" style="left:153px"><div class="avatar" role="img" aria-label="Customer portrait"></div>"My family has been very fortunate to have access to super fresh organic fruit and veggies at a..."<br>– Jess Holloway (Chatter),<br>03/05/2014</div>
    <div class="quote" style="left:289px"><div class="avatar" role="img" aria-label="Customer portrait"></div>"My family has been very fortunate to have access to super fresh organic fruit and veggies at a..."<br>– Jess Holloway (Chatter),<br>03/05/2014</div>
    <div class="viewmore">View More<span class="arrowbox" style="background:var(--purple);width:13px;height:13px"><svg width="5" height="7"><path d="M1 1 4 3.5 1 6" fill="none" stroke="#fff" stroke-width="1.3"/></svg></span></div>
  </section>
</main>

<div class="social" style="left:528px;top:1040px">
  <i style="background:var(--navy)">Ch</i><i style="background:var(--sky)">Cl</i><i style="background:#8fc6e3">Lw</i><i style="background:#d8302f">Cs</i><i style="background:#1fb0e8">Tw</i>
</div>

<footer>
  <div class="col" style="left:154px"><h4>My account</h4>Sign in<br>Create account</div>
  <div class="col" style="left:266px"><h4>Our Store</h4>Contact us<br>Sitemap</div>
  <div class="col" style="left:364px"><h4>Customer Service</h4>About your order<br>About Fern Meadow Co<br>What is Fern Meadow?<br>Privacy policy</div>
  <div class="col" style="left:503px;width:130px"><h4>Stay Connected</h4>Enter your email address to receive special offers and promotions.</div>
  <div class="subscribe"><div class="field">your email</div><div class="send">send</div></div>
</footer>

<div class="legal">
  <p>© 2004-2014 Fern Meadow Co.  Powered by Earth loving hippies like you!</p>
  <div class="payments"><span>Paylink</span><span>Coinpurse</span><span>Swiftpay</span><span>Cardora</span><span>Vantix</span></div>
</div>
</body>
</html>
```